Branded Flyer Template Libraries Brightwater Lending

Create one-page flyer templates for equipment finance industry to provide a fast turnaround that consistent on-brand for educational and promotional flyers that can be quickly customized with partners logos. These will become a standard toolkit for marketing for use in Adobe Illustrator and editable. customer facing are business owners considering equipment financing typically used for leave behind flyers, email, and handouts. vendor facing to equipment dealers, manufacturers and sales reps who refer customers to us, typically used at trade shows, co branded flyers, and email promotions.
Requesting 1-2 flyer templates with concepts for educational, and promotional.
Brand guide and current flyers in circulation are uploaded as reference.
Look and feel
Each slider illustrates characteristics of the customer's brand and the style your logo design should communicate.

```html
<!DOCTYPE html>
<html lang="en">
<head>
<meta charset="utf-8">
<title>Brightwater Lending – Equipment Finance Flyer</title>
<link href="https://fonts.googleapis.com/css2?family=Merriweather:wght@700;900&family=Rubik:wght@400;500&display=swap" rel="stylesheet">
<style>
  :root {
    --backdrop: #c2c2c2;
    --forest: #0f4c27;
    --brand-green: #17602f;
    --leaf: #2e9a2e;
    --sage: #a5cf7e;
    --sage-light: #dcefc8;
    --ink: #111;
    --white: #fff;
    --card-bg: rgba(240, 244, 240, 0.9);
  }
  * { margin: 0; padding: 0; box-sizing: border-box; }
  html, body { width: 1200px; height: 1200px; overflow: hidden; background: var(--backdrop); }
  body { font-family: "Rubik", Arial, sans-serif; position: relative; }

  .flyer {
    position: absolute; left: 175px; top: 50px; width: 850px; height: 1100px;
    background: var(--white); overflow: hidden;
  }
  .hero-photo {
    position: absolute; left: 0; top: 90px; width: 850px; height: 640px;
    background:
      linear-gradient(180deg, #fff 0%, rgba(255,255,255,0) 14%),
      linear-gradient(180deg, #cfe6f4 0%, #e8f1ea 42%, #f4e6b0 50%, #8fbf4e 56%, #5c9a2c 70%, #3f7f22 100%);
  }
  .hero-photo .farmer-area {
    position: absolute; right: 60px; top: 190px; width: 230px; height: 380px;
    background: linear-gradient(180deg, rgba(214,150,70,0.55), rgba(160,110,50,0.45));
    border-radius: 110px 110px 20px 20px;
  }

  .brand { position: absolute; left: 60px; top: 40px; display: flex; align-items: center; gap: 10px; }
  .brand-dot { width: 58px; height: 58px; border-radius: 50%; background: var(--brand-green); }
  .brand-name { font-family: "Merriweather", Georgia, serif; font-weight: 700; font-size: 20px; color: var(--brand-green); letter-spacing: 0.3px; }
  .brand-tag { font-size: 7px; letter-spacing: 3px; color: var(--ink); text-align: center; margin-top: 3px; }

  .headline { position: absolute; left: 56px; top: 122px; font-family: "Merriweather", Georgia, serif; font-weight: 900; line-height: 1; }
  .headline .lead { display: block; font-size: 82px; color: var(--forest); }
  .headline .rest { display: block; font-size: 56px; color: var(--ink); margin-top: 4px; line-height: 1.05; }

  .waves { position: absolute; left: 0; top: 0; }

  .about-card {
    position: absolute; left: 52px; top: 408px; width: 317px; height: 332px;
    background: var(--card-bg); border: 3px solid var(--leaf); border-radius: 22px;
    padding: 28px 28px 0 30px;
  }
  .about-card h2 { font-family: "Merriweather", Georgia, serif; font-weight: 900; font-size: 24px; color: var(--brand-green); margin-bottom: 6px; }
  .about-card p { font-size: 12.6px; line-height: 16.4px; color: var(--ink); margin-bottom: 17px; }

  .photo-ring { position: absolute; border-radius: 50%; background: var(--sage); }
  .photo-ring .photo { position: absolute; border-radius: 50%; border: 2px solid var(--forest); }
  .ring-meeting { left: 384px; top: 508px; width: 218px; height: 218px; }
  .ring-meeting .photo { left: 17px; top: 17px; width: 184px; height: 184px; background: linear-gradient(160deg, #b7c3cc, #7f8c86 55%, #3f4a52); }
  .ring-tractor { left: 581px; top: 535px; width: 232px; height: 232px; }
  .ring-tractor .photo { left: 19px; top: 19px; width: 194px; height: 194px; background: radial-gradient(circle at 45% 30%, #f7d77a, #e39a34 40%, #8a4a26 75%, #5a3220); }

  .section-title { font-family: "Merriweather", Georgia, serif; font-weight: 700; font-size: 23px; color: var(--white); position: absolute; }
  .section-title .accent { color: var(--sage); }
  .why-title { left: 52px; top: 757px; }
  .highlights-title { left: 358px; top: 757px; }

  .why-list { position: absolute; left: 56px; top: 795px; list-style: none; }
  .why-list li { display: flex; gap: 9px; font-size: 12px; line-height: 12px; color: var(--white); margin-bottom: 8px; }
  .why-list svg { flex: none; margin-top: 1px; }

  .highlight-card {
    position: absolute; top: 800px; width: 147px; height: 120px;
    background: var(--sage); border-radius: 12px; padding: 14px 8px 0 37px;
    font-size: 11.8px; line-height: 15px; color: var(--ink);
  }
  .highlight-card .num {
    position: absolute; left: 2px; top: 2px; width: 30px; height: 28px; border-radius: 50%;
    background: var(--forest); color: var(--white); font-family: "Merriweather", Georgia, serif;
    font-weight: 700; font-size: 12px; display: flex; align-items: center; justify-content: center;
  }
  .hc-1 { left: 359px; } .hc-2 { left: 513px; } .hc-3 { left: 665px; }

  .tagline { position: absolute; left: 52px; top: 936px; font-family: "Merriweather", Georgia, serif; font-weight: 700; font-size: 22px; line-height: 28px; color: var(--white); }
  .tagline .accent { color: var(--sage); }
  .divider { position: absolute; left: 323px; top: 926px; }
  .pitch { position: absolute; left: 358px; top: 937px; width: 452px; font-size: 11.3px; line-height: 15px; color: var(--white); }

  .rule { position: absolute; left: 52px; top: 1016px; width: 755px; height: 1px; background: rgba(255,255,255,0.6); }
  .contact { position: absolute; top: 1039px; left: 52px; width: 755px; display: flex; justify-content: space-between; font-weight: 500; font-size: 16px; color: var(--white); }
  .contact span { display: flex; align-items: center; gap: 6px; }
</style>
</head>
<body>
<div class="flyer">
  <div class="hero-photo" role="img" aria-label="Photo of a farmer in a straw hat using a tablet in a sunlit vegetable field">
    <div class="farmer-area"></div>
  </div>

  <div class="brand">
    <div class="brand-dot"></div>
    <div>
      <div class="brand-name">BRIGHTWATER LENDING</div>
      <div class="brand-tag">— EQUIPMENT FINANCE —</div>
    </div>
  </div>

  <h1 class="headline">
    <span class="lead">Financing</span>
    <span class="rest">That Flexes<br>With You</span>
  </h1>

  <svg class="waves" width="850" height="1100" viewBox="0 0 850 1100" aria-hidden="true">
    <path d="M0,595 Q260,700 520,640 Q700,600 850,660 L850,1100 L0,1100Z" fill="#a5cf7e"/>
    <path d="M0,615 Q260,720 520,665 Q700,625 850,700 L850,1100 L0,1100Z" fill="#fff"/>
    <path d="M0,622 Q260,728 520,672 Q700,635 850,712 L850,1100 L0,1100Z" fill="#a5cf7e"/>
    <path d="M0,660 Q240,760 520,700 Q700,665 850,745 L850,1100 L0,1100Z" fill="#0f4c27"/>
    <path d="M780,640 Q830,680 850,745 L850,720 Q830,670 790,640Z" fill="#1a9a2a"/>
  </svg>

  <section class="about-card">
    <h2>ABOUT US</h2>
    <p>At Brightwater Lending, we’re more than an equipment financing company. We’re a team built on faith, trust, and a genuine commitment to doing business the right way. Since 1996, we’ve partnered with customers and vendors nationwide to create financing solutions that help people and businesses thrive.</p>
    <p>With 30 solid years of expertise and a foundation built on integrity, we are proud to continue doing what we love each and succeed.</p>
  </section>

  <div class="photo-ring ring-meeting">
    <div class="photo" role="img" aria-label="Photo of a dealer and a farmer reviewing paperwork beside farm equipment"></div>
  </div>
  <div class="photo-ring ring-tractor">
    <div class="photo" role="img" aria-label="Photo of a tractor working a field at sunset"></div>
  </div>

  <h3 class="section-title why-title"><span class="accent">Why</span> Choose Us?</h3>
  <ul class="why-list">
    <li><svg width="10" height="10" viewBox="0 0 10 10"><circle cx="5" cy="5" r="5" fill="#a5cf7e"/><path d="M2.6,5.2 L4.3,6.8 L7.4,3.4" stroke="#0f4c27" stroke-width="1.4" fill="none"/></svg>Lorem ipsus sinctio riatent ulluptae<br>nis ium sedit</li>
    <li><svg width="10" height="10" viewBox="0 0 10 10"><circle cx="5" cy="5" r="5" fill="#a5cf7e"/><path d="M2.6,5.2 L4.3,6.8 L7.4,3.4" stroke="#0f4c27" stroke-width="1.4" fill="none"/></svg>Lorem ipsus sinctio riatent ulluptae<br>nis ium sedit</li>
    <li><svg width="10" height="10" viewBox="0 0 10 10"><circle cx="5" cy="5" r="5" fill="#a5cf7e"/><path d="M2.6,5.2 L4.3,6.8 L7.4,3.4" stroke="#0f4c27" stroke-width="1.4" fill="none"/></svg>Lorem ipsus sinctio riatent ulluptae<br>nis ium sedit</li>
    <li><svg width="10" height="10" viewBox="0 0 10 10"><circle cx="5" cy="5" r="5" fill="#a5cf7e"/><path d="M2.6,5.2 L4.3,6.8 L7.4,3.4" stroke="#0f4c27" stroke-width="1.4" fill="none"/></svg>Lorem ipsus sinctio riatent ulluptae<br>nis ium sedit</li>
  </ul>

  <h3 class="section-title highlights-title">Highlights</h3>
  <div class="highlight-card hc-1"><span class="num">01</span>Lorem Ipsum<br>is simply<br>dummy text<br>of the printing<br>and typesetting<br>industry.</div>
  <div class="highlight-card hc-2"><span class="num">02</span>Lorem Ipsum<br>is simply<br>dummy text<br>of the printing<br>and typesetting<br>industry.</div>
  <div class="highlight-card hc-3"><span class="num">03</span>Lorem Ipsum<br>is simply<br>dummy text<br>of the printing<br>and typesetting<br>industry.</div>

  <div class="tagline"><span class="accent">Financing for</span><br>Hardworking Buyers</div>
  <svg class="divider" width="10" height="58" viewBox="0 0 10 58" aria-hidden="true">
    <line x1="1" y1="0" x2="1" y2="58" stroke="#fff" stroke-width="1.5"/>
    <path d="M1,24 L7,28 L1,32Z" fill="#fff"/>
  </svg>
  <p class="pitch">Brightwater Lending makes financing simple. Our team gets to know you so we can tailor solutions to your unique needs. For decades, customers nationwide have trusted us because we do what we say. It all starts with a conversation—tell us what you’re looking for.</p>

  <div class="rule"></div>
  <div class="contact">
    <span><svg width="14" height="14" viewBox="0 0 24 24"><path d="M6.6 10.8a15.1 15.1 0 0 0 6.6 6.6l2.2-2.2c.3-.3.7-.4 1-.2 1.1.4 2.3.6 3.6.6.6 0 1 .4 1 1V20c0 .6-.4 1-1 1A17 17 0 0 1 3 4c0-.6.4-1 1-1h3.5c.6 0 1 .4 1 1 0 1.3.2 2.5.6 3.6.1.3 0 .7-.2 1z" fill="#a5cf7e"/></svg>800-555-0142</span>
    <span><svg width="12" height="16" viewBox="0 0 12 16"><path d="M6,0 C2.7,0 0,2.6 0,5.9 C0,10.3 6,16 6,16 C6,16 12,10.3 12,5.9 C12,2.6 9.3,0 6,0Z" fill="#a5cf7e"/><circle cx="6" cy="6" r="2.2" fill="#0f4c27"/></svg>120 Harbor Road North, Lakeview, MN 56000</span>
    <span><svg width="15" height="15" viewBox="0 0 16 16" fill="none" stroke="#a5cf7e" stroke-width="1.3"><circle cx="8" cy="8" r="7"/><ellipse cx="8" cy="8" rx="3" ry="7"/><line x1="1" y1="8" x2="15" y2="8"/><line x1="2.5" y1="4.5" x2="13.5" y2="4.5"/><line x1="2.5" y1="11.5" x2="13.5" y2="11.5"/></svg>brightwaterlending.com</span>
  </div>
</div>
</body>
</html>
```